A wedding company selling top 5 wedding venues in an affluent historic Florida Town

We need a word press design (Layered PSD files) to hand over to a web developer.
It's for Maple Hollow Nuptial Company. The company has been set up to sell wedding packages to the top 5 or so wedding venues in Maple Hollow. Maple Hollow is an historic Florida town which is known for it's European village feel, with paved roads and sidewalk seating for cafe's and restaurants.
Needs to be clean and fresh with an elegant feel.
We have a logo already established which you will find attached to the brief along with a few wedding photo's from a couple of the venues we will be selling.
We are starting with 4 venues, which will each have about 3 different packages. I'd like a design for a home page and an inside page.
We will have a blog, recent weddings page which we will update with photo's etc.
The home page will have tabs for:
Wedding Venues, Reception Venues, About US, Contact US, Blog,

Target Market(s)

Brides and Grooms looking for a stylish elegant wedding. Based in western speaking countries, aged between 20 - 50 years old. Probably more aimed at the female who makes the decisions.

Industry/Entity Type

Wedding

Font styles to use
Sans Serif

Colors

Designer to choose colors to be used in the design.

Requirements
Must have
• On the home page I'd like a big slider, A block with a paragraph about Maple Hollow in general, a twitter feed, a recent weddings link and a big button on each page which goes to a "request info" form.

```html
<!DOCTYPE html>
<html lang="en">
<head>
<meta charset="utf-8">
<title>Maple Hollow Nuptial Company</title>
<link rel="stylesheet" href="https://fonts.googleapis.com/css2?family=Open+Sans:wght@400;600&family=Raleway:wght@200&display=swap">
<style>
  :root {
    --ink: #3a3a3a;
    --ink-soft: #555555;
    --rule: rgba(120, 110, 110, 0.28);
    --panel: rgba(255, 248, 246, 0.55);
    --logo: #7a3f8f;
    --icon: #8c8c8c;
    --disc: rgba(255, 255, 255, 0.32);
    --btn-light: rgba(255, 255, 255, 0.82);
    --btn-dark: #3b3b3b;
  }
  * { margin: 0; padding: 0; box-sizing: border-box; }
  html, body { width: 1200px; height: 750px; overflow: hidden; }
  body { font-family: "Open Sans", Verdana, sans-serif; color: var(--ink); }

  .stage { position: relative; width: 1200px; height: 750px; overflow: hidden; }

  .hero-photo {
    position: absolute; inset: 0;
    background:
      radial-gradient(ellipse 240px 200px at 640px 300px, #f4f1e6 0%, rgba(244,241,230,0) 100%),
      radial-gradient(ellipse 140px 120px at 480px 600px, #e9b8bc 0%, rgba(233,184,188,0) 100%),
      radial-gradient(ellipse 130px 120px at 1030px 380px, #eab9bb 0%, rgba(234,185,187,0) 100%),
      radial-gradient(ellipse 470px 380px at 640px 380px, #eef0df 0%, #e4e7cf 55%, rgba(228,231,207,0) 100%),
      radial-gradient(ellipse 160px 220px at 1140px 260px, #d9e2e0 0%, rgba(217,226,224,0) 100%),
      linear-gradient(90deg, #e8d6cc 0%, #f1e6e0 35%, #ede7e2 70%, #cfc3bc 100%);
  }

  .sidebar {
    position: absolute; left: 0; top: 0; width: 158px; height: 750px;
    background: var(--panel);
    border-right: 1px solid rgba(255,255,255,0.5);
  }

  .brand { position: absolute; left: 22px; top: 56px; width: 120px; display: flex; align-items: center; gap: 6px; }
  .brand-dot { width: 10px; height: 10px; border-radius: 50%; background: var(--logo); flex: none; }
  .brand-name { font-size: 13px; line-height: 17px; font-weight: 600; color: var(--logo); }

  .main-nav { position: absolute; left: 22px; top: 162px; width: 114px; list-style: none; }
  .main-nav li { height: 30.7px; border-bottom: 1px solid var(--rule); display: flex; align-items: center; padding-left: 7px; font-size: 9.5px; text-transform: uppercase; color: var(--ink); }

  .search { position: absolute; left: 22px; top: 345px; width: 114px; height: 21px; border: 1px solid rgba(120,110,110,0.45); background: rgba(255,255,255,0.25); display: flex; align-items: center; justify-content: space-between; padding: 0 5px 0 7px; font-size: 9.5px; color: var(--ink-soft); }

  .sub-nav { position: absolute; left: 22px; top: 384px; width: 114px; list-style: none; }
  .sub-nav li { height: 30px; border-bottom: 1px solid var(--rule); display: flex; align-items: center; padding-left: 7px; font-size: 9.5px; text-transform: uppercase; color: var(--ink); }

  .social { position: absolute; left: 22px; top: 668px; display: flex; gap: 5px; }
  .social span { width: 18px; height: 18px; border-radius: 50%; background: var(--icon); }
  .legal { position: absolute; left: 22px; top: 695px; width: 110px; font-size: 7.5px; line-height: 10px; text-transform: uppercase; color: var(--ink-soft); }

  .slide-disc {
    position: absolute; left: 426px; top: 120px; width: 505px; height: 505px; border-radius: 50%;
    background: var(--disc);
    border: 1px solid rgba(255,255,255,0.45);
  }
  .slide-title {
    position: absolute; left: 476px; top: 236px;
    font-family: "Raleway", "Helvetica Neue", sans-serif; font-weight: 200;
    font-size: 80px; line-height: 70px; letter-spacing: 2px; color: #2e2e2e; text-transform: uppercase;
  }
  .slide-text {
    position: absolute; left: 445px; top: 401px; width: 468px;
    font-size: 14px; line-height: 24.5px; text-align: center; color: var(--ink);
  }
  .slide-controls { position: absolute; left: 619px; top: 521px; display: flex; gap: 9px; }
  .slide-btn { width: 57px; height: 57px; border-radius: 50%; display: flex; align-items: center; justify-content: center; }
  .slide-btn--prev { background: var(--btn-light); }
  .slide-btn--next { background: var(--btn-dark); }
</style>
</head>
<body>
<div class="stage">
  <div class="hero-photo" role="img" aria-label="Close-up photograph of a bride holding a round bouquet of white and blush pink roses"></div>

  <aside class="sidebar">
    <div class="brand">
      <span class="brand-dot"></span>
      <span class="brand-name">Maple Hollow Nuptial Company</span>
    </div>

    <ul class="main-nav">
      <li>Weding Venues</li>
      <li>Reception Venues</li>
      <li>About Us</li>
      <li>Blog</li>
      <li>Contact Us</li>
    </ul>

    <div class="search">
      <span>Search...</span>
      <svg width="11" height="11" viewBox="0 0 11 11" aria-hidden="true"><circle cx="4.5" cy="4.5" r="3.5" fill="none" stroke="#777" stroke-width="1.2"/><line x1="7.2" y1="7.2" x2="10.3" y2="10.3" stroke="#777" stroke-width="1.3"/></svg>
    </div>

    <ul class="sub-nav">
      <li>Request Info &#x2228;</li>
      <li>Recent Wedding &#x2228;</li>
    </ul>

    <div class="social" aria-label="Social links">
      <span></span><span></span><span></span><span></span><span></span>
    </div>
    <p class="legal">2014 XYZ. All rights reserved.</p>
  </aside>

  <section class="slide">
    <div class="slide-disc"></div>
    <h1 class="slide-title">Maple<br>Hollow</h1>
    <p class="slide-text">Integer ultrices ipsum id justo ultrices sed blandit felis ultricies. Duis semper tristique congue. Pellentesque id orci sed ligula elementum tempor ut non nulla. Aenean lectus nulla, rutrum in tincidunt non, vestibulum a arcu ...</p>
    <div class="slide-controls">
      <span class="slide-btn slide-btn--prev">
        <svg width="14" height="16" viewBox="0 0 14 16" aria-label="Previous"><polyline points="10,2 4,8 10,14" fill="none" stroke="#333" stroke-width="1.4"/></svg>
      </span>
      <span class="slide-btn slide-btn--next">
        <svg width="14" height="16" viewBox="0 0 14 16" aria-label="Next"><polyline points="4,2 10,8 4,14" fill="none" stroke="#fff" stroke-width="1.4"/></svg>
      </span>
    </div>
  </section>
</div>
</body>
</html>
```